Brookvale Ridge College

We are looking to update our current webpage at www.brookvaleridge.ca. We would like to make it modern, fresh and appealing to students. We want to keep our logo the same with the logo colours blended in as the primary colours and focus. We are open to reconfiguring content as well.
Reason: Hi, In the next 3 days we will have narrowed our search to 3 designs and will make a choice before the final deadline...
Industry/Entity Type
College

```html
<!DOCTYPE html>
<html lang="en">
<head>
<meta charset="utf-8">
<title>Brookvale Ridge College</title>
<link rel="stylesheet" href="https://fonts.googleapis.com/css2?family=Quicksand:wght@400;500;600&family=Roboto:wght@400;500&family=Playfair+Display:ital@1&display=swap">
<style>
:root{
  --green:#0b5a50;
  --green-dark:#063f38;
  --navy:#1c2f6b;
  --heading:#155a52;
  --text:#666666;
  --nav-bg:#efefef;
  --line:#e2e2e2;
  --white:#ffffff;
}
*{margin:0;padding:0;box-sizing:border-box}
html,body{width:770px;height:1200px;overflow:hidden;background:var(--white)}
body{position:relative;font-family:"Quicksand",sans-serif;color:var(--text)}
.abs{position:absolute}
.topline{left:0;top:0;width:770px;height:3px;background:var(--green-dark)}
.utility{right:48px;top:3px;display:flex;gap:2px}
.utility a{background:var(--green);color:var(--white);font:500 7px "Roboto",sans-serif;text-transform:uppercase;text-decoration:none;height:19px;line-height:19px;padding:0 7px}
.brand{left:48px;top:20px;display:flex;align-items:center;gap:8px}
.brand-mark{width:16px;height:16px;border-radius:50%;background:var(--navy)}
.brand-name{font:600 15px/1 "Quicksand",sans-serif;color:var(--navy);width:118px}
.tagline{left:200px;top:33px;font:500 14px "Quicksand",sans-serif;color:var(--navy);letter-spacing:.3px}
.connect{right:48px;top:35px;display:flex;align-items:center;gap:4px}
.connect span{font:500 7px "Roboto",sans-serif;color:var(--navy);margin-right:4px}
.connect i{width:19px;height:19px;border-radius:50%;display:block}
.nav{left:0;top:64px;width:770px;height:29px;background:var(--nav-bg)}
.nav ul{list-style:none;display:flex;margin-left:48px;height:29px}
.nav li{font:400 7.6px/29px "Roboto",sans-serif;color:#333;text-transform:uppercase;padding:0 8.6px}
.nav li.active{background:var(--navy);color:var(--white);padding:0 14px}
.hero{left:0;top:93px;width:770px;height:265px;background:linear-gradient(100deg,#2e2420 0%,#5b4a3c 30%,#8a7a64 55%,#b7a98f 80%,#9a8a72 100%)}
.hero-word{right:52px;top:90px;font:italic 62px/1 "Playfair Display",serif;color:var(--white);letter-spacing:2px}
.dots{left:362px;top:244px;display:flex;gap:5px}
.dots i{width:7px;height:7px;border-radius:50%;background:var(--white);display:block}
.dots i:first-child{background:#4a8f86}
.band{left:0;width:770px;border-bottom:2px solid var(--line)}
.welcome{top:358px;height:188px}
.welcome-photo{left:0;top:0;width:284px;height:186px;clip-path:polygon(0 0,284px 0,256px 186px,0 186px);background:linear-gradient(135deg,#6f8a78,#2a2a2a 55%,#c9a98f)}
.welcome-title{left:284px;width:444px;top:22px;text-align:center;font:500 15px/19px "Quicksand",sans-serif;color:var(--heading);text-transform:uppercase}
.welcome-body{left:291px;width:431px;top:66px;text-align:center;font:500 7.4px/13.6px "Quicksand",sans-serif}
.btn{background:var(--navy);color:var(--white);font:500 7.5px "Roboto",sans-serif;text-transform:uppercase;text-align:center;height:23px;line-height:23px}
.news{top:546px;height:188px}
.news-photo{right:0;top:0;width:284px;height:186px;clip-path:polygon(0 0,284px 0,284px 186px,30px 186px);background:linear-gradient(120deg,#1a1410,#6b4a2c 50%,#c0894e 75%,#2a1d14)}
.section-title{font:500 15px "Quicksand",sans-serif;color:var(--heading);text-transform:uppercase}
.arrows{display:flex;gap:10px}
.news-sub{left:48px;top:48px;font:500 10px "Quicksand",sans-serif;color:var(--navy)}
.news-body{left:48px;top:64px;width:430px;font:500 7.4px/13.6px "Quicksand",sans-serif}
.admission{top:734px;height:190px}
.admission-panel{left:0;top:0;width:280px;height:188px;clip-path:polygon(0 0,280px 0,252px 188px,0 188px);background:radial-gradient(circle at 20% 40%,#1d7a6d,var(--green) 50%,var(--green-dark))}
.admission ul{list-style:none;left:48px;top:48px}
.admission li{font:500 8.2px/17.2px "Quicksand",sans-serif;color:var(--white);display:flex;align-items:center;gap:9px}
.thumb{width:130px;height:84px;border:3px solid var(--white);box-shadow:0 2px 4px rgba(0,0,0,.25)}
.caption{width:130px;text-align:center;font:500 10.5px "Quicksand",sans-serif;color:var(--navy)}
.campus{top:924px;height:190px}
.campus-photo{right:0;top:0;width:280px;height:188px;clip-path:polygon(0 0,280px 0,280px 188px,28px 188px);background:linear-gradient(160deg,#d8d4cc,#a4988a 40%,#4b4a55 70%,#7a3b3b)}
.footer{left:0;top:1114px;width:770px;height:86px;background:linear-gradient(#e6e6e6,#f8f8f8)}
.footer .addr{top:28px;width:770px;text-align:center;font:400 7.8px "Roboto",sans-serif;color:#555}
.footer .copy{top:49px;width:770px;text-align:center;font:500 6.6px "Roboto",sans-serif;color:var(--green);text-transform:uppercase}
</style>
</head>
<body>
<div class="abs topline"></div>
<nav class="abs utility"><a>Apply Today</a><a>Donate</a><a>Library</a><a>Text for Info</a></nav>
<div class="abs brand"><span class="brand-mark"></span><span class="brand-name">Brookvale Ridge College</span></div>
<div class="abs tagline">educate. equip. enrich</div>
<div class="abs connect"><span>CONNECT US:</span><i style="background:#3b5998"></i><i style="background:#3aa3e3"></i><i style="background:#555"></i><i style="background:#f18b1f"></i><i style="background:#e52d27"></i></div>
<nav class="abs nav"><ul>
<li class="active">Home</li><li>About Us</li><li>Consider Brookvale</li><li>Current Student</li><li>Current Students</li><li>Alumni</li><li>Supporters</li><li>News &amp; Events</li><li>Brookvale Park</li><li>Contact Us</li>
</ul></nav>

<section class="abs hero" role="img" aria-label="Photo of a graduate in cap and gown talking with a guest at commencement">
  <div class="abs hero-word">EDUCATE</div>
  <div class="abs dots"><i></i><i></i><i></i><i></i></div>
</section>

<section class="abs band welcome">
  <div class="abs welcome-photo" role="img" aria-label="Photo of smiling graduates in caps and gowns"></div>
  <h1 class="abs welcome-title">Welcome to Brookvale Ridge<br>Brookvale Ridge College</h1>
  <p class="abs welcome-body">Aliquam molestie, mi et imperdiet euismod, dui purus auctor tellus, et interdum lacus lectus et ante. Sed accumsan sollicitudin sapien, sit amet adipiscing turpis gravida ac. In congue, neque ac lobortis volutpat, libero mauris varius mi, vitae suscipit ipsum ligula vitae risus. Duis aliquam nibh a dui iaculis viverra id a velit. Vivamus egestas risus in magna varius commodo. Sed semper viverra egestas. Etiam pretium porttitor lectus, vel ornare neque porta volutpat.</p>
  <div class="abs btn" style="left:468px;top:138px;width:76px">Read More</div>
</section>

<section class="abs band news">
  <div class="abs news-photo" role="img" aria-label="Photo of a student playing drums in a warmly lit studio"></div>
  <h2 class="abs section-title" style="left:48px;top:22px">News &amp; Events</h2>
  <div class="abs arrows" style="left:446px;top:27px">
    <svg width="9" height="12" viewBox="0 0 9 12"><path d="M7 1 2 6l5 5" fill="none" stroke="#777" stroke-width="1.3"/></svg>
    <svg width="9" height="12" viewBox="0 0 9 12"><path d="M2 1l5 5-5 5" fill="none" stroke="#333" stroke-width="1.3"/></svg>
  </div>
  <h3 class="abs news-sub">Sound Production and Media</h3>
  <p class="abs news-body">Brookvale Ridge College is pleased to offer a one year program that is geared towards equipping a music student with skills for sound production, media, and church ministry. In addition to music, audio, media and song writing courses, the student will study Bible and spiritual formation issues. "Hands on" application in the recording lab as well as in chapel services will provide experience in areas of interest. Some elective space is available for those interested in a ministry group [auditions required] or in taking private music lessons.</p>
  <div class="abs btn" style="left:48px;top:146px;width:76px">Read More</div>
</section>

<section class="abs band admission">
  <div class="abs admission-panel"></div>
  <h2 class="abs section-title" style="left:48px;top:22px;color:var(--white)">Admission</h2>
  <ul class="abs">
    <li><svg width="8" height="7" viewBox="0 0 8 7"><path d="M1 3.5 3 5.5 7 1" fill="none" stroke="#fff" stroke-width="1.6"/></svg>Download the full Catalogue</li>
    <li><svg width="8" height="7" viewBox="0 0 8 7"><path d="M1 3.5 3 5.5 7 1" fill="none" stroke="#fff" stroke-width="1.6"/></svg>Apply Today (Application Package)</li>
    <li><svg width="8" height="7" viewBox="0 0 8 7"><path d="M1 3.5 3 5.5 7 1" fill="none" stroke="#fff" stroke-width="1.6"/></svg>Information Request</li>
    <li><svg width="8" height="7" viewBox="0 0 8 7"><path d="M1 3.5 3 5.5 7 1" fill="none" stroke="#fff" stroke-width="1.6"/></svg>Browse our Programs</li>
    <li><svg width="8" height="7" viewBox="0 0 8 7"><path d="M1 3.5 3 5.5 7 1" fill="none" stroke="#fff" stroke-width="1.6"/></svg>Download Forms</li>
    <li><svg width="8" height="7" viewBox="0 0 8 7"><path d="M1 3.5 3 5.5 7 1" fill="none" stroke="#fff" stroke-width="1.6"/></svg>Admissions Information</li>
    <li><svg width="8" height="7" viewBox="0 0 8 7"><path d="M1 3.5 3 5.5 7 1" fill="none" stroke="#fff" stroke-width="1.6"/></svg>Campus Directory</li>
  </ul>
  <h2 class="abs section-title" style="left:302px;top:22px">Brookvale Videos</h2>
  <div class="abs arrows" style="left:696px;top:27px">
    <svg width="9" height="12" viewBox="0 0 9 12"><path d="M7 1 2 6l5 5" fill="none" stroke="#777" stroke-width="1.3"/></svg>
    <svg width="9" height="12" viewBox="0 0 9 12"><path d="M2 1l5 5-5 5" fill="none" stroke="#333" stroke-width="1.3"/></svg>
  </div>
  <div class="abs thumb" style="left:302px;top:56px;background:linear-gradient(#2a2a2a,#7a2a2a 60%,#3a3a3a)" role="img" aria-label="Video still of graduates on stage receiving diplomas"></div>
  <div class="abs thumb" style="left:448px;top:56px;background:linear-gradient(#b8ab99,#8a7a6a)" role="img" aria-label="Video still of students sitting together in a lounge"></div>
  <div class="abs thumb" style="left:594px;top:56px;background:linear-gradient(#1f2430,#4a4e5a 60%,#2a2a30)" role="img" aria-label="Video still of a band performing on a stage with a screen"></div>
  <div class="abs caption" style="left:302px;top:154px">The Future is Bright</div>
  <div class="abs caption" style="left:448px;top:154px">Campus Tour</div>
  <div class="abs caption" style="left:594px;top:154px">Music Program</div>
</section>

<section class="abs band campus">
  <div class="abs campus-photo" role="img" aria-label="Photo of a cheerful group of students posing together"></div>
  <h2 class="abs section-title" style="left:0;width:504px;text-align:center;top:22px">Our Campus</h2>
  <div class="abs thumb" style="left:47px;top:57px;background:linear-gradient(135deg,#c9d9b8,#e8ece4)" role="img" aria-label="Street map showing directions to campus"></div>
  <div class="abs thumb" style="left:193px;top:57px;background:linear-gradient(135deg,#3a4a78,#4e6a5e)" role="img" aria-label="Aerial campus map with location markers"></div>
  <div class="abs thumb" style="left:338px;top:57px;background:linear-gradient(135deg,#e0d8cc,#2a2a2a 60%,#c9a94a)" role="img" aria-label="Photo of a graduate celebrating in cap and gown"></div>
  <div class="abs caption" style="left:47px;top:160px">Map &amp; Directions</div>
  <div class="abs caption" style="left:193px;top:160px">Campus Map</div>
  <div class="abs caption" style="left:338px;top:160px">Photo Tour</div>
</section>

<footer class="abs footer">
  <p class="abs addr">BROOKVALE RIDGE COLLEGE • 1480 LARCHMONT ROAD • PO BOX 2200 • FERNHOLLOW • BC • CANADA • V0X 1A0 • 1-800-555-0142 • (604) 555-0187</p>
  <p class="abs copy">Copyright © 2014. All Right Reserved</p>
</footer>
</body>
</html>
```